Summer Camp Postcard

Martial Arts Summer Camp

Harbor Crest Martial Arts
275 Route 18
Central Valley, NY 10917
www.HCMAstudios.example

Logo previously uploaded

```html
<!DOCTYPE html>
<html lang="en">
<head>
<meta charset="utf-8">
<title>Harbor Crest Martial Arts – Summer Camp Postcard</title>
<link href="https://fonts.googleapis.com/css2?family=Exo+2:ital,wght@0,700;0,800;1,700&family=Roboto+Condensed:wght@400;700&display=swap" rel="stylesheet">
<style>
  :root {
    --red: #e5283a;
    --blue: #2a5fb0;
    --black: #121212;
    --navy: #0d1f47;
    --white: #ffffff;
    --stamp: #9a9a9a;
    --page: #ece8e1;
  }
  * { margin: 0; padding: 0; box-sizing: border-box; }
  html, body { width: 889px; height: 1200px; overflow: hidden; }
  body {
    background: var(--page);
    position: relative;
    font-family: "Roboto Condensed", sans-serif;
  }
  .postcard {
    position: absolute;
    left: 73px;
    width: 742px;
    background: var(--white);
    overflow: hidden;
    box-shadow: 0 3px 10px rgba(0,0,0,.25);
  }
  .postcard--front { top: 82px; height: 498px; }
  .postcard--back { top: 623px; height: 496px; }
  .postcard__art { position: absolute; inset: 0; width: 100%; height: 100%; }

  /* brand mark */
  .brand { position: absolute; display: flex; align-items: center; gap: 7px; }
  .brand__dot { width: 26px; height: 26px; border-radius: 50%; background: var(--red); }
  .brand__name { font-family: "Roboto Condensed", sans-serif; font-weight: 700; font-size: 34px; letter-spacing: 1px; }
  .brand--front { left: 20px; top: 150px; }
  .brand--front .brand__name { color: var(--white); }
  .brand--back { left: 385px; top: 42px; }
  .brand--back .brand__name { color: var(--black); }

  .call-us { position: absolute; left: 28px; top: 222px; color: var(--red); font-family: "Exo 2", sans-serif; font-weight: 800; font-size: 21px; }
  .call-phone { position: absolute; left: 28px; top: 251px; color: var(--white); font-weight: 700; font-size: 20px; }

  .headline { position: absolute; right: 26px; top: 18px; text-align: right; font-family: "Exo 2", sans-serif; }
  .headline__lead { color: var(--white); font-style: italic; font-weight: 700; font-size: 30px; line-height: 1.05; }
  .headline__big { color: var(--black); font-weight: 800; font-size: 46px; line-height: 1.1; }

  .invite { position: absolute; left: 468px; width: 260px; top: 196px; text-align: center; color: var(--black); font-weight: 700; }
  .invite__main { font-size: 17px; }
  .invite__sub { font-size: 12.5px; margin-top: 3px; }

  .contact { position: absolute; list-style: none; color: var(--white); font-size: 13.5px; }
  .contact li { display: flex; align-items: center; gap: 7px; height: 20.5px; }
  .contact svg { width: 11px; height: 11px; flex: none; }
  .contact--front { right: 14px; top: 414px; }
  .contact--front li { flex-direction: row-reverse; justify-content: flex-start; }
  .contact--back { left: 30px; top: 397px; font-size: 13px; }

  .reasons { position: absolute; left: 26px; top: 28px; list-style: none; color: var(--white); font-size: 17px; line-height: 24.5px; }
  .reasons li { position: relative; padding-left: 20px; margin-bottom: 2.5px; }
  .reasons li::before { content: ""; position: absolute; left: 3px; top: 9px; width: 7px; height: 7px; border-radius: 50%; background: var(--white); }

  .cta { position: absolute; left: 30px; top: 274px; font-weight: 700; }
  .cta__lead { color: var(--navy); font-size: 15.5px; line-height: 20px; }
  .cta__main { color: var(--white); font-size: 21px; line-height: 27px; }

  .stamp-box { position: absolute; left: 625px; top: 13px; width: 101px; height: 106px; background: var(--stamp); }
</style>
</head>
<body>

<section class="postcard postcard--front">
  <svg class="postcard__art" viewBox="0 0 742 498">
    <defs>
      <linearGradient id="kidsPhoto" x1="0" y1="0" x2="1" y2="1">
        <stop offset="0" stop-color="#2b2b2b"/>
        <stop offset=".5" stop-color="#5a3a36"/>
        <stop offset="1" stop-color="#1b1b1b"/>
      </linearGradient>
      <linearGradient id="classPhoto" x1="0" y1="0" x2="0" y2="1">
        <stop offset="0" stop-color="#b07a5a"/><stop offset="1" stop-color="#6a4a3a"/>
      </linearGradient>
      <linearGradient id="boyPhoto" x1="0" y1="0" x2="0" y2="1">
        <stop offset="0" stop-color="#f2ece6"/><stop offset="1" stop-color="#cfc6be"/>
      </linearGradient>
      <linearGradient id="groupPhoto" x1="0" y1="0" x2="0" y2="1">
        <stop offset="0" stop-color="#e3b9a0"/><stop offset="1" stop-color="#8e6a80"/>
      </linearGradient>
    </defs>
    <rect class="header-band" x="0" y="0" width="742" height="174" fill="var(--red)"/>
    <rect x="0" y="174" width="742" height="7" fill="var(--blue)"/>
    <rect x="0" y="397" width="742" height="6" fill="var(--red)"/>
    <rect class="contact-band" x="0" y="405" width="742" height="93" fill="var(--black)"/>
    <path d="M0 0 H298 Q592 250 364 498 H0 Z" fill="var(--blue)"/>
    <path d="M0 0 H285 Q578 250 351 498 H0 Z" fill="var(--red)"/>
    <path d="M0 0 H272 Q564 250 338 498 H0 Z" fill="url(#kidsPhoto)" role="img" aria-label="Photo: two smiling children in red martial arts uniforms striking a pose in front of a dark brick wall"/>
    <circle cx="512" cy="321" r="35" fill="url(#classPhoto)" stroke="var(--red)" stroke-width="3" role="img" aria-label="Photo: a martial arts class training in a studio"/>
    <circle cx="595" cy="321" r="50" fill="url(#boyPhoto)" stroke="var(--red)" stroke-width="3" role="img" aria-label="Photo: a boy in a white uniform in a fighting stance"/>
    <circle cx="676" cy="321" r="35" fill="url(#groupPhoto)" stroke="var(--red)" stroke-width="3" role="img" aria-label="Photo: a group of smiling students"/>
  </svg>

  <div class="brand brand--front"><span class="brand__dot"></span><span class="brand__name">HCMA</span></div>
  <p class="call-us">CALL US</p>
  <p class="call-phone">845-555-0142</p>

  <div class="headline">
    <p class="headline__lead">Summer Time</p>
    <p class="headline__lead">Is Martial Arts</p>
    <p class="headline__big">FUN TIME!</p>
  </div>

  <div class="invite">
    <p class="invite__main">Your child is invited to join</p>
    <p class="invite__sub">the fun with a free beginner’s course!</p>
  </div>

  <ul class="contact contact--front">
    <li><svg viewBox="0 0 12 12"><path d="M2 1 L4.5 1 L5 4 L3.6 5 Q5 8 7 8.4 L8 7 L11 7.5 L11 10 Q6 11.5 2.5 7 Q0.5 4 2 1 Z" fill="var(--red)"/></svg><span>845-555-0142</span></li>
    <li><svg viewBox="0 0 12 12"><rect x="0.5" y="2" width="11" height="8" fill="var(--red)"/><path d="M0.5 2 L6 6.5 L11.5 2" stroke="var(--white)" fill="none"/></svg><span>mrivera@harborcrest.example</span></li>
    <li><svg viewBox="0 0 12 12"><circle cx="6" cy="6" r="5.5" fill="var(--red)"/><path d="M0.5 6 H11.5 M6 0.5 V11.5" stroke="var(--black)" stroke-width="0.8"/><ellipse cx="6" cy="6" rx="2.5" ry="5.5" stroke="var(--black)" stroke-width="0.8" fill="none"/></svg><span>HarborCrestMA@mail.example</span></li>
  </ul>
</section>

<section class="postcard postcard--back">
  <svg class="postcard__art" viewBox="0 0 742 496">
    <defs>
      <linearGradient id="kickPhoto" x1="0" y1="0" x2="0" y2="1">
        <stop offset="0" stop-color="#f4efe9"/><stop offset="1" stop-color="#d9d2ca"/>
      </linearGradient>
    </defs>
    <path d="M0 0 H292 Q498 130 436 272 H0 Z" fill="var(--blue)"/>
    <path d="M0 0 H278 Q484 130 422 272 H0 Z" fill="var(--red)"/>
    <path class="ribbon" d="M0 264 H444 L424 312 L444 360 H0 Z" fill="var(--blue)"/>
    <path d="M410 360 Q392 432 372 496" stroke="var(--blue)" stroke-width="7" fill="none"/>
    <rect x="0" y="363" width="406" height="6" fill="var(--red)"/>
    <path class="contact-band" d="M0 371 H404 Q386 436 366 496 H0 Z" fill="var(--black)"/>
    <rect x="238" y="351" width="132" height="145" fill="url(#kickPhoto)" role="img" aria-label="Photo: a young girl in a white uniform performing a high kick"/>
  </svg>

  <ul class="reasons">
    <li>Summer is a time to be<br>active and healthy</li>
    <li>Summer is a time to be<br>safer, with self-defense training.</li>
    <li>Summer is a time to grow as<br>a leader</li>
    <li>Summer is a time to gain<br>self-confidence and improve<br>your focus for next school year</li>
  </ul>

  <div class="cta">
    <p class="cta__lead">Call our school today and give your child</p>
    <p class="cta__main">a summer filled with fun and important<br>lessons only martial arts can teach</p>
  </div>

  <ul class="contact contact--back">
    <li><svg viewBox="0 0 12 12"><path d="M2 1 L4.5 1 L5 4 L3.6 5 Q5 8 7 8.4 L8 7 L11 7.5 L11 10 Q6 11.5 2.5 7 Q0.5 4 2 1 Z" fill="var(--red)"/></svg><span>845-555-0142</span></li>
    <li><svg viewBox="0 0 12 12"><rect x="0.5" y="2" width="11" height="8" fill="var(--red)"/><path d="M0.5 2 L6 6.5 L11.5 2" stroke="var(--white)" fill="none"/></svg><span>mrivera@harborcrest.example</span></li>
    <li><svg viewBox="0 0 12 12"><rect x="0.5" y="2" width="11" height="8" fill="var(--red)"/><path d="M0.5 2 L6 6.5 L11.5 2" stroke="var(--white)" fill="none"/></svg><span>HarborCrestMA@mail.example</span></li>
    <li><svg viewBox="0 0 12 12"><circle cx="6" cy="6" r="5.5" fill="var(--red)"/><path d="M0.5 6 H11.5 M6 0.5 V11.5" stroke="var(--black)" stroke-width="0.8"/><ellipse cx="6" cy="6" rx="2.5" ry="5.5" stroke="var(--black)" stroke-width="0.8" fill="none"/></svg><span>HarborCrestMA@mail.example</span></li>
  </ul>

  <div class="brand brand--back"><span class="brand__dot"></span><span class="brand__name">HCMA</span></div>
  <div class="stamp-box"></div>
</section>

</body>
</html>
```